Lumen Drive Health Business card

We want a business card that matches our business theme. Our website is www.swiftcarehub.example
The company name is Lumen Drive Health
The persons having the business cards will be doctors
My logo is attached.
We have a drive-thru medical center where our motto is Fast, Reliable, and Convenient. Our goal is to change the medical space while utilizing technologies, keeping a professional and clean look

Medical

Info on the card should be: Name, Position, Cell number, website, email address, possibly the office line as well

Requirements
Must have
• Logo
Nice to have
• Professional medical feel with our logo colors incorporated

```html
<!DOCTYPE html>
<html lang="en">
<head>
<meta charset="utf-8">
<title>Lumen Drive Health – Business Card</title>
<link rel="stylesheet" href="https://fonts.googleapis.com/css2?family=Montserrat:ital,wght@0,500;0,800;1,500&family=Open+Sans:wght@400;600&display=swap">
<style>
  :root {
    --brand-blue: #1b48a0;
    --brand-sky: #3cc4f0;
    --paper: #ffffff;
    --backdrop: #1d1e21;
    --ink-dark: #111827;
  }
  * { box-sizing: border-box; margin: 0; padding: 0; }
  html, body { width: 1200px; height: 900px; overflow: hidden; background: var(--backdrop); }
  .canvas {
    width: 1200px; height: 900px;
    display: flex; flex-direction: column; align-items: center; justify-content: center; gap: 40px;
  }
  .card {
    position: relative; width: 700px; height: 400px; border-radius: 22px; overflow: hidden;
    background: var(--brand-blue);
    box-shadow: 0 18px 40px rgba(0,0,0,.5);
  }
  .card__shape { position: absolute; inset: 0; }

  .brand__name {
    position: absolute; font-family: "Montserrat", sans-serif; font-weight: 800; line-height: 1.05;
  }
  .brand__tagline {
    position: absolute; font-family: "Open Sans", sans-serif; font-weight: 400;
    letter-spacing: .08em; white-space: nowrap;
  }

  /* front */
  .front .brand__name { top: 46px; left: 400px; width: 260px; font-size: 34px; color: var(--brand-blue); }
  .front .brand__tagline { top: 146px; left: 402px; font-size: 14px; color: var(--ink-dark); }

  .holder { position: absolute; left: 20px; top: 252px; width: 285px; text-align: right; }
  .holder__name {
    font-family: "Montserrat", sans-serif; font-weight: 800; font-size: 28px;
    color: var(--brand-sky); letter-spacing: .03em; white-space: nowrap;
  }
  .holder__role {
    font-family: "Montserrat", sans-serif; font-style: italic; font-weight: 500;
    font-size: 16px; color: var(--paper); margin-top: 4px;
  }
  .divider { position: absolute; left: 322px; top: 252px; width: 1px; height: 108px; background: var(--brand-sky); }
  .contact { position: absolute; left: 340px; top: 254px; list-style: none; }
  .contact__item {
    display: flex; align-items: center; gap: 10px; height: 26px;
    font-family: "Open Sans", sans-serif; font-size: 15px; color: var(--paper); white-space: nowrap;
  }
  .contact__icon { width: 14px; height: 14px; flex: none; }

  /* back */
  .back .brand__name {
    top: 118px; left: 0; right: 0; text-align: center; font-size: 54px; color: var(--paper);
  }
  .back .brand__tagline { top: 272px; left: 0; right: 0; text-align: center; font-size: 19px; color: var(--paper); }
</style>
</head>
<body>
<main class="canvas">

  <section class="card front" aria-label="Business card front">
    <svg class="card__shape" viewBox="0 0 700 400" aria-hidden="true">
      <path d="M180 0 H700 V270 C600 228 480 205 360 205 C290 150 250 60 180 0 Z" fill="var(--paper)"/>
      <path d="M205 100 C265 130 310 165 360 205" fill="none" stroke="var(--brand-sky)" stroke-width="6" stroke-linecap="round"/>
      <path d="M360 205 C470 205 560 220 650 250" fill="none" stroke="var(--brand-sky)" stroke-width="4" stroke-linecap="round"/>
    </svg>

    <p class="brand__name">Lumen Drive Health</p>
    <p class="brand__tagline">CARE I TRUST I ACCESS</p>

    <div class="holder">
      <h1 class="holder__name">MARCUS DELANE</h1>
      <p class="holder__role">CEO/Founder</p>
    </div>
    <span class="divider"></span>
    <ul class="contact">
      <li class="contact__item">
        <svg class="contact__icon" viewBox="0 0 24 24"><path d="M6 2l4 4-2 3c1 3 4 6 7 7l3-2 4 4-3 4C10 22 2 14 2 5z" fill="var(--brand-sky)"/></svg>
        +1 (555) 014-2231
      </li>
      <li class="contact__item">
        <svg class="contact__icon" viewBox="0 0 24 24"><rect x="6" y="2" width="12" height="20" rx="2" fill="none" stroke="var(--brand-sky)" stroke-width="2"/><circle cx="12" cy="18" r="1.3" fill="var(--brand-sky)"/></svg>
        +1 (555) 019-4470
      </li>
      <li class="contact__item">
        <svg class="contact__icon" viewBox="0 0 24 24"><rect x="2" y="5" width="20" height="14" rx="1" fill="var(--brand-sky)"/><path d="M2 6l10 7 10-7" fill="none" stroke="var(--brand-blue)" stroke-width="1.6"/></svg>
        info@swiftcarehub.example
      </li>
      <li class="contact__item">
        <svg class="contact__icon" viewBox="0 0 24 24"><circle cx="12" cy="12" r="9" fill="none" stroke="var(--brand-sky)" stroke-width="2"/><path d="M3 12h18M12 3c-4 5-4 13 0 18M12 3c4 5 4 13 0 18" fill="none" stroke="var(--brand-sky)" stroke-width="1.5"/></svg>
        www.swiftcarehub.example
      </li>
    </ul>
  </section>

  <section class="card back" aria-label="Business card back">
    <p class="brand__name">Lumen Drive<br>Health</p>
    <p class="brand__tagline">CARE I TRUST I ACCESS</p>
  </section>

</main>
</body>
</html>
```